Web app UI design

This web app has been built and the UI needs a refresh.

Attached are the pages which need the refresh.

The web app is for a cyber security product/service and customers are inputting their details.

```html
<!DOCTYPE html>
<html lang="en">
<head>
<meta charset="utf-8">
<title>Vaultra – App Screens</title>
<link href="https://fonts.googleapis.com/css2?family=Montserrat:wght@300;400;500;600;700&family=Roboto:wght@400;500&display=swap" rel="stylesheet">
<style>
:root{
  --canvas:#a3a3a3;
  --navy:#2d3250;
  --navy-dark:#222638;
  --navy-active:#41465f;
  --white:#ffffff;
  --panel-grey:#f2f2f4;
  --text:#2d3250;
  --text-body:#4a4a4a;
  --text-muted:#9a9a9a;
  --line:#e6e6ea;
  --ok:#46b24a;
  --bad:#e8504a;
  --teal:#5fd6b8;
}
*{box-sizing:border-box;margin:0;padding:0}
html,body{width:1200px;height:4329px;overflow:hidden}
body{background:var(--canvas);font-family:'Montserrat',sans-serif;color:var(--text);position:relative}

.screen{position:absolute;left:28px;width:1143px;height:817px;background:var(--navy);overflow:hidden}

/* hero */
.hero-art{position:absolute;inset:0;background:
  radial-gradient(ellipse 420px 180px at 330px 640px,rgba(95,214,184,.55),rgba(95,214,184,0) 70%),
  radial-gradient(ellipse 520px 140px at 700px 520px,rgba(95,214,184,.22),rgba(95,214,184,0) 70%),
  radial-gradient(ellipse 300px 200px at 120px 760px,rgba(95,214,184,.35),rgba(95,214,184,0) 70%),
  var(--navy)}
.hero-logo{position:absolute;top:222px;left:0;right:0;text-align:center;font-weight:300;font-size:54px;letter-spacing:.18em;color:var(--white);padding-left:.18em}
.hero-sub{position:absolute;top:313px;left:0;right:0;text-align:center;font-weight:500;font-size:29px;color:var(--white)}
.hero-search{position:absolute;left:282px;top:402px;width:577px;height:54px;background:var(--white);border-radius:27px}
.hero-search .placeholder{position:absolute;left:29px;top:18px;font-size:12px;color:#555}
.hero-search .btn{position:absolute;right:0;top:0;width:143px;height:54px;border-radius:27px;background:var(--navy-dark);border:3px solid var(--white);color:var(--white);font-weight:600;font-size:16px;display:flex;align-items:center;justify-content:center}

/* app chrome */
.brand{position:absolute;left:39px;top:22px;font-weight:300;font-size:34px;letter-spacing:.2em;color:#e3e6ee}
.top-icons{position:absolute;top:24px;left:919px;display:flex;align-items:center;gap:12px}
.icon-btn{width:37px;height:37px;display:flex;align-items:center;justify-content:center}
.avatar{position:absolute;left:1064px;top:24px;width:37px;height:37px;border-radius:50%;background:linear-gradient(160deg,#8b8f9b,#4e5364)}
.avatar::after{content:"";position:absolute;right:-2px;top:-2px;width:11px;height:11px;border-radius:50%;background:var(--ok);border:2px solid var(--navy)}

.side-nav{position:absolute;left:0;top:111px;width:232px}
.side-nav a{display:flex;align-items:center;height:44px;margin-bottom:13px;padding-left:38px;color:var(--white);text-decoration:none;font-weight:600;font-size:15px;gap:20px}
.side-nav a.active{background:var(--navy-active)}
.side-nav svg{width:20px;height:20px;flex:none}

.content{position:absolute;left:232px;top:84px;right:0;bottom:0;background:var(--white);border-radius:46px 40px 0 0}
.page-title{position:absolute;top:40px;left:0;right:0;text-align:center;font-weight:600;font-size:40px;color:var(--text)}
.footer{position:absolute;left:0;right:0;top:669px;border-top:1px solid var(--line);text-align:center;padding-top:21px;font-weight:600;font-size:14px;color:var(--text)}

/* cards */
.card{position:absolute;background:var(--white);border-radius:16px;box-shadow:0 2px 14px rgba(0,0,0,.09);overflow:hidden}
.card-head{height:69px;background:var(--navy-dark);color:var(--white);font-weight:600;font-size:22px;display:flex;align-items:center;justify-content:center;border-radius:16px 16px 0 0}
.note-list{list-style:none;position:absolute;left:27px;right:20px;top:131px;font-family:'Roboto',sans-serif;font-size:13px;color:var(--text-body);line-height:24px}
.note-list li{display:flex;gap:12px;margin-bottom:16px}
.note-list li::before{content:"»";color:#777}
.guide-lead{position:absolute;left:27px;top:90px;font-weight:500;font-size:13.5px;color:#222}
.step{position:absolute;left:22px;display:flex;gap:12px;font-family:'Roboto',sans-serif;font-size:13.5px;color:var(--text-muted)}
.step .dot{width:14px;height:14px;border-radius:50%;flex:none;margin-top:2px;display:flex;align-items:center;justify-content:center}
.step .dot.ok{background:var(--ok)}
.step .dot.bad{background:var(--bad)}
.step strong{display:block;font-weight:400;color:#444}
.step small{display:block;font-size:11px;color:#aaa;margin-top:2px}

/* forms */
.form-box{position:absolute;left:54px;top:141px;background:var(--panel-grey);border-radius:22px}
.form-lead{position:absolute;left:47px;top:48px;font-weight:500;font-size:16px;color:#333}
.field{position:absolute;height:59px;width:366px;background:var(--white);border-radius:6px;box-shadow:0 1px 6px rgba(0,0,0,.07);font-family:'Roboto',sans-serif;font-size:12px;color:#555;padding:22px 22px}
.pill-btn{position:absolute;height:45px;border-radius:23px;background:var(--navy);color:var(--white);font-weight:600;font-size:14px;display:flex;align-items:center;justify-content:center}

/* subscription */
.sub-bg{position:absolute;inset:0;border-radius:46px 40px 0 0;background:
  radial-gradient(ellipse 380px 260px at 700px 420px,rgba(160,170,185,.55),rgba(160,170,185,0) 70%),
  linear-gradient(160deg,#eef1f5,#dfe3ea 60%,#e9ecf1)}
.plan{position:absolute;top:104px;width:252px;height:383px}
.plan .card-head{height:77px;font-size:22px;border-radius:12px 12px 0 0}
.plan.bronze .card-head{background:linear-gradient(180deg,#d8a85e,#86582b)}
.plan.silver .card-head{background:linear-gradient(180deg,#ececec,#9b9b9b)}
.plan.gold .card-head{background:linear-gradient(180deg,#f4e47c,#bf982c)}
.perk{position:absolute;left:20px;right:12px;display:flex;gap:12px;font-family:'Roboto',sans-serif;font-size:11.5px;color:#333;line-height:19px}
.perk .tick{width:12px;height:12px;border-radius:50%;background:var(--navy-dark);flex:none;margin-top:4px;display:flex;align-items:center;justify-content:center}
.price{position:absolute;left:20px;top:243px;font-weight:700;font-size:18px;color:#222}
.price.text{font-weight:600}
.period{position:absolute;left:20px;top:272px;font-family:'Roboto',sans-serif;font-size:10px;color:#444}
.plan .pill-btn{left:20px;top:311px;width:173px;height:47px}
.pill-btn.outline{background:var(--white);color:#222;border:1.5px solid var(--navy)}

/* verify info */
.info-row{position:absolute;left:50px;display:flex;font-size:13px}
.info-row b{width:237px;font-weight:600;color:#333}
.info-row span{font-family:'Roboto',sans-serif;color:var(--text-muted)}
.label{position:absolute;font-size:13px;color:#333;font-weight:500}
.round-field{position:absolute;height:50px;background:var(--white);border:1px solid #e2e2e6;border-radius:25px;font-family:'Roboto',sans-serif;font-size:12px;color:#999;padding:17px 22px}
.check-line{position:absolute;left:47px;top:325px;display:flex;align-items:center;gap:10px;font-family:'Roboto',sans-serif;font-size:13px;color:var(--text-muted)}
.check-line .box{width:17px;height:17px;border:1.5px solid #888;border-radius:3px;display:flex;align-items:center;justify-content:center}
</style>
</head>
<body>

<!-- Screen 1: search landing -->
<section class="screen" style="top:32px">
  <div class="hero-art" role="img" aria-label="Dark navy backdrop with glowing teal data particles and small padlock symbols"></div>
  <div class="hero-logo">VAULTRA</div>
  <h1 class="hero-sub">Search using companies name, ABN or ACN</h1>
  <div class="hero-search">
    <span class="placeholder">Name / ABN / ACN</span>
    <span class="btn">Search</span>
  </div>
</section>

<!-- Screen 2: home -->
<section class="screen" style="top:879px">
  <div class="brand">VAULTRA</div>
  <div class="top-icons">
    <span class="icon-btn"><svg width="37" height="37" viewBox="0 0 37 37"><circle cx="18.5" cy="18.5" r="16" fill="none" stroke="#fff" stroke-width="2"/><circle cx="17" cy="17" r="5" fill="none" stroke="#fff" stroke-width="2.2"/><line x1="20.5" y1="20.5" x2="24" y2="24" stroke="#fff" stroke-width="2.4" stroke-linecap="round"/></svg></span>
    <span class="icon-btn"><svg width="22" height="22" viewBox="0 0 24 24"><path d="M12 3a6 6 0 0 0-6 6v5l-2 3h16l-2-3V9a6 6 0 0 0-6-6z" fill="#fff"/><circle cx="12" cy="20" r="2.2" fill="#fff"/></svg></span>
    <span class="icon-btn"><svg width="26" height="20" viewBox="0 0 26 20"><rect y="2" width="26" height="2.2" fill="#fff"/><rect y="9" width="26" height="2.2" fill="#fff"/><rect y="16" width="26" height="2.2" fill="#fff"/></svg></span>
  </div>
  <div class="avatar" role="img" aria-label="User profile photo"></div>
  <nav class="side-nav">
    <a class="active"><svg viewBox="0 0 24 24" fill="none" stroke="#fff" stroke-width="1.6"><path d="M3 11l9-7 9 7v9h-6v-6H9v6H3z"/></svg>Home</a>
    <a><svg viewBox="0 0 24 24" fill="none" stroke="#fff" stroke-width="1.6"><circle cx="12" cy="8" r="4"/><path d="M4 21c1-5 4-7 8-7s7 2 8 7"/></svg>Profile</a>
    <a><svg viewBox="0 0 24 24" fill="none" stroke="#fff" stroke-width="1.6"><path d="M5 7a9 9 0 0 1 15 3M19 17a9 9 0 0 1-15-3"/><path d="M14.5 9.5c-.5-1-1.5-1.5-2.5-1.5-1.4 0-2.5.8-2.5 2s1 1.7 2.5 2 2.5.9 2.5 2-1.1 2-2.5 2c-1 0-2-.5-2.5-1.5M12 6.5v11"/></svg>Subscription</a>
    <a><svg viewBox="0 0 24 24" fill="none" stroke="#fff" stroke-width="1.6"><path d="M12 2l2.5 2 3.2-.3.6 3.1 2.7 1.8-1.3 2.9 1.3 2.9-2.7 1.8-.6 3.1-3.2-.3L12 22l-2.5-2-3.2.3-.6-3.1-2.7-1.8 1.3-2.9-1.3-2.9 2.7-1.8.6-3.1 3.2.3z"/><path d="M8 12l3 3 5-6"/></svg>Verify</a>
  </nav>
  <main class="content">
    <h2 class="page-title">Vaultra</h2>
    <article class="card" style="left:54px;top:141px;width:392px;height:313px">
      <div class="card-head">Welcome</div>
      <ul class="note-list">
        <li>Thank you for signing up with Vaultra.</li>
        <li>We are launching in a few weeks and will contact you shortly.</li>
      </ul>
    </article>
    <article class="card" style="left:476px;top:141px;width:390px;height:373px">
      <div class="card-head">Setup Guide</div>
      <p class="guide-lead">Please follow the below steps to get started</p>
      <div class="step" style="top:150px"><span class="dot ok"><svg width="8" height="8" viewBox="0 0 8 8"><path d="M1 4l2 2 4-4" stroke="#fff" stroke-width="1.5" fill="none"/></svg></span><div>Register Account</div></div>
      <div class="step" style="top:190px"><span class="dot ok"><svg width="8" height="8" viewBox="0 0 8 8"><path d="M1 4l2 2 4-4" stroke="#fff" stroke-width="1.5" fill="none"/></svg></span><div><strong>Update Profile</strong><small>Setup basic account information</small></div></div>
      <div class="step" style="top:244px"><span class="dot ok"><svg width="8" height="8" viewBox="0 0 8 8"><path d="M1 4l2 2 4-4" stroke="#fff" stroke-width="1.5" fill="none"/></svg></span><div><strong>Select Subscription</strong><small>Select and setup subscription type</small></div></div>
      <div class="step" style="top:298px"><span class="dot bad"><svg width="8" height="8" viewBox="0 0 8 8"><path d="M2 2l4 4M6 2l-4 4" stroke="#fff" stroke-width="1.4"/></svg></span><div>Setup details to protect</div></div>
      <div class="step" style="top:330px"><span class="dot bad"><svg width="8" height="8" viewBox="0 0 8 8"><path d="M2 2l4 4M6 2l-4 4" stroke="#fff" stroke-width="1.4"/></svg></span><div>Account Active</div></div>
    </article>
    <footer class="footer">Vaultra @ 2023</footer>
  </main>
</section>

<!-- Screen 3: profile -->
<section class="screen" style="top:1740px">
  <div class="brand">VAULTRA</div>
  <div class="top-icons">
    <span class="icon-btn"><svg width="37" height="37" viewBox="0 0 37 37"><circle cx="18.5" cy="18.5" r="16" fill="none" stroke="#fff" stroke-width="2"/><circle cx="17" cy="17" r="5" fill="none" stroke="#fff" stroke-width="2.2"/><line x1="20.5" y1="20.5" x2="24" y2="24" stroke="#fff" stroke-width="2.4" stroke-linecap="round"/></svg></span>
    <span class="icon-btn"><svg width="22" height="22" viewBox="0 0 24 24"><path d="M12 3a6 6 0 0 0-6 6v5l-2 3h16l-2-3V9a6 6 0 0 0-6-6z" fill="#fff"/><circle cx="12" cy="20" r="2.2" fill="#fff"/></svg></span>
    <span class="icon-btn"><svg width="26" height="20" viewBox="0 0 26 20"><rect y="2" width="26" height="2.2" fill="#fff"/><rect y="9" width="26" height="2.2" fill="#fff"/><rect y="16" width="26" height="2.2" fill="#fff"/></svg></span>
  </div>
  <div class="avatar" role="img" aria-label="User profile photo"></div>
  <nav class="side-nav">
    <a><svg viewBox="0 0 24 24" fill="none" stroke="#fff" stroke-width="1.6"><path d="M3 11l9-7 9 7v9h-6v-6H9v6H3z"/></svg>Home</a>
    <a class="active"><svg viewBox="0 0 24 24" fill="none" stroke="#fff" stroke-width="1.6"><circle cx="12" cy="8" r="4"/><path d="M4 21c1-5 4-7 8-7s7 2 8 7"/></svg>Profile</a>
    <a><svg viewBox="0 0 24 24" fill="none" stroke="#fff" stroke-width="1.6"><path d="M5 7a9 9 0 0 1 15 3M19 17a9 9 0 0 1-15-3"/><path d="M14.5 9.5c-.5-1-1.5-1.5-2.5-1.5-1.4 0-2.5.8-2.5 2s1 1.7 2.5 2 2.5.9 2.5 2-1.1 2-2.5 2c-1 0-2-.5-2.5-1.5M12 6.5v11"/></svg>Subscription</a>
    <a><svg viewBox="0 0 24 24" fill="none" stroke="#fff" stroke-width="1.6"><path d="M12 2l2.5 2 3.2-.3.6 3.1 2.7 1.8-1.3 2.9 1.3 2.9-2.7 1.8-.6 3.1-3.2-.3L12 22l-2.5-2-3.2.3-.6-3.1-2.7-1.8 1.3-2.9-1.3-2.9 2.7-1.8.6-3.1 3.2.3z"/><path d="M8 12l3 3 5-6"/></svg>Verify</a>
  </nav>
  <main class="content">
    <h2 class="page-title">Profile</h2>
    <div class="form-box" style="width:825px;height:455px">
      <p class="form-lead">Only your company name, ACN and ABN from below will be shared on your profile.</p>
      <div class="field" style="left:34px;top:108px">Email</div>
      <div class="field" style="left:423px;top:108px">Company</div>
      <div class="field" style="left:34px;top:188px">ACN</div>
      <div class="field" style="left:423px;top:188px">ABN</div>
      <div class="field" style="left:34px;top:271px">Phone</div>
      <span class="pill-btn" style="left:47px;top:363px;width:171px">Save Profile</span>
    </div>
    <footer class="footer">Vaultra @ 2023</footer>
  </main>
</section>

<!-- Screen 4: subscription -->
<section class="screen" style="top:2595px">
  <div class="brand">VAULTRA</div>
  <div class="top-icons">
    <span class="icon-btn"><svg width="37" height="37" viewBox="0 0 37 37"><circle cx="18.5" cy="18.5" r="16" fill="none" stroke="#fff" stroke-width="2"/><circle cx="17" cy="17" r="5" fill="none" stroke="#fff" stroke-width="2.2"/><line x1="20.5" y1="20.5" x2="24" y2="24" stroke="#fff" stroke-width="2.4" stroke-linecap="round"/></svg></span>
    <span class="icon-btn"><svg width="22" height="22" viewBox="0 0 24 24"><path d="M12 3a6 6 0 0 0-6 6v5l-2 3h16l-2-3V9a6 6 0 0 0-6-6z" fill="#fff"/><circle cx="12" cy="20" r="2.2" fill="#fff"/></svg></span>
    <span class="icon-btn"><svg width="26" height="20" viewBox="0 0 26 20"><rect y="2" width="26" height="2.2" fill="#fff"/><rect y="9" width="26" height="2.2" fill="#fff"/><rect y="16" width="26" height="2.2" fill="#fff"/></svg></span>
  </div>
  <div class="avatar" role="img" aria-label="User profile photo"></div>
  <nav class="side-nav">
    <a><svg viewBox="0 0 24 24" fill="none" stroke="#fff" stroke-width="1.6"><path d="M3 11l9-7 9 7v9h-6v-6H9v6H3z"/></svg>Home</a>
    <a><svg viewBox="0 0 24 24" fill="none" stroke="#fff" stroke-width="1.6"><circle cx="12" cy="8" r="4"/><path d="M4 21c1-5 4-7 8-7s7 2 8 7"/></svg>Profile</a>
    <a class="active"><svg viewBox="0 0 24 24" fill="none" stroke="#fff" stroke-width="1.6"><path d="M5 7a9 9 0 0 1 15 3M19 17a9 9 0 0 1-15-3"/><path d="M14.5 9.5c-.5-1-1.5-1.5-2.5-1.5-1.4 0-2.5.8-2.5 2s1 1.7 2.5 2 2.5.9 2.5 2-1.1 2-2.5 2c-1 0-2-.5-2.5-1.5M12 6.5v11"/></svg>Subscription</a>
    <a><svg viewBox="0 0 24 24" fill="none" stroke="#fff" stroke-width="1.6"><path d="M12 2l2.5 2 3.2-.3.6 3.1 2.7 1.8-1.3 2.9 1.3 2.9-2.7 1.8-.6 3.1-3.2-.3L12 22l-2.5-2-3.2.3-.6-3.1-2.7-1.8 1.3-2.9-1.3-2.9 2.7-1.8.6-3.1 3.2.3z"/><path d="M8 12l3 3 5-6"/></svg>Verify</a>
  </nav>
  <main class="content">
    <div class="sub-bg" role="img" aria-label="Soft pale photo of hands typing on a laptop keyboard"></div>

    <article class="card plan bronze" style="left:47px">
      <div class="card-head">Bronze</div>
      <div class="perk" style="top:116px"><span class="tick"><svg width="7" height="7" viewBox="0 0 8 8"><path d="M1 4l2 2 4-4" stroke="#fff" stroke-width="1.6" fill="none"/></svg></span>Access to verification system</div>
      <div class="perk" style="top:151px"><span class="tick"><svg width="7" height="7" viewBox="0 0 8 8"><path d="M1 4l2 2 4-4" stroke="#fff" stroke-width="1.6" fill="none"/></svg></span>Use of Vaultra logo and material on website and documents</div>
      <div class="perk" style="top:207px"><span class="tick"><svg width="7" height="7" viewBox="0 0 8 8"><path d="M1 4l2 2 4-4" stroke="#fff" stroke-width="1.6" fill="none"/></svg></span>Other perks..</div>
      <div class="price">$85</div>
      <div class="period">Monthly</div>
      <span class="pill-btn outline">Subscribed</span>
    </article>

    <article class="card plan silver" style="left:334px">
      <div class="card-head">Silver</div>
      <div class="perk" style="top:116px"><span class="tick"><svg width="7" height="7" viewBox="0 0 8 8"><path d="M1 4l2 2 4-4" stroke="#fff" stroke-width="1.6" fill="none"/></svg></span>Bronze plan +</div>
      <div class="perk" style="top:151px"><span class="tick"><svg width="7" height="7" viewBox="0 0 8 8"><path d="M1 4l2 2 4-4" stroke="#fff" stroke-width="1.6" fill="none"/></svg></span>Cyber insurance in case of event</div>
      <div class="perk" style="top:185px"><span class="tick"><svg width="7" height="7" viewBox="0 0 8 8"><path d="M1 4l2 2 4-4" stroke="#fff" stroke-width="1.6" fill="none"/></svg></span>Debicated support to remediate events</div>
      <div class="price text">Contact us for price</div>
      <div class="period">Monthly</div>
      <span class="pill-btn">Contact</span>
    </article>

    <article class="card plan gold" style="left:620px">
      <div class="card-head">Gold</div>
      <div class="perk" style="top:116px"><span class="tick"><svg width="7" height="7" viewBox="0 0 8 8"><path d="M1 4l2 2 4-4" stroke="#fff" stroke-width="1.6" fill="none"/></svg></span>Silver plan +</div>
      <div class="perk" style="top:151px"><span class="tick"><svg width="7" height="7" viewBox="0 0 8 8"><path d="M1 4l2 2 4-4" stroke="#fff" stroke-width="1.6" fill="none"/></svg></span>Cybersecurity expert on retainer</div>
      <div class="perk" style="top:180px"><span class="tick"><svg width="7" height="7" viewBox="0 0 8 8"><path d="M1 4l2 2 4-4" stroke="#fff" stroke-width="1.6" fill="none"/></svg></span>System reviews</div>
      <div class="perk" style="top:210px"><span class="tick"><svg width="7" height="7" viewBox="0 0 8 8"><path d="M1 4l2 2 4-4" stroke="#fff" stroke-width="1.6" fill="none"/></svg></span>Phone consultations</div>
      <div class="price text">Contact us for price</div>
      <div class="period">Monthly</div>
      <span class="pill-btn">Contact</span>
    </article>

    <span class="pill-btn" style="left:47px;top:535px;width:205px">Manage Subscription</span>
    <footer class="footer">Vaultra @ 2023</footer>
  </main>
</section>

<!-- Screen 5: verify info -->
<section class="screen" style="top:3457px">
  <div class="brand">VAULTRA</div>
  <div class="top-icons">
    <span class="icon-btn"><svg width="37" height="37" viewBox="0 0 37 37"><circle cx="18.5" cy="18.5" r="16" fill="none" stroke="#fff" stroke-width="2"/><circle cx="17" cy="17" r="5" fill="none" stroke="#fff" stroke-width="2.2"/><line x1="20.5" y1="20.5" x2="24" y2="24" stroke="#fff" stroke-width="2.4" stroke-linecap="round"/></svg></span>
    <span class="icon-btn"><svg width="22" height="22" viewBox="0 0 24 24"><path d="M12 3a6 6 0 0 0-6 6v5l-2 3h16l-2-3V9a6 6 0 0 0-6-6z" fill="#fff"/><circle cx="12" cy="20" r="2.2" fill="#fff"/></svg></span>
    <span class="icon-btn"><svg width="26" height="20" viewBox="0 0 26 20"><rect y="2" width="26" height="2.2" fill="#fff"/><rect y="9" width="26" height="2.2" fill="#fff"/><rect y="16" width="26" height="2.2" fill="#fff"/></svg></span>
  </div>
  <div class="avatar" role="img" aria-label="User profile photo"></div>
  <nav class="side-nav">
    <a><svg viewBox="0 0 24 24" fill="none" stroke="#fff" stroke-width="1.6"><path d="M3 11l9-7 9 7v9h-6v-6H9v6H3z"/></svg>Home</a>
    <a><svg viewBox="0 0 24 24" fill="none" stroke="#fff" stroke-width="1.6"><circle cx="12" cy="8" r="4"/><path d="M4 21c1-5 4-7 8-7s7 2 8 7"/></svg>Profile</a>
    <a><svg viewBox="0 0 24 24" fill="none" stroke="#fff" stroke-width="1.6"><path d="M5 7a9 9 0 0 1 15 3M19 17a9 9 0 0 1-15-3"/><path d="M14.5 9.5c-.5-1-1.5-1.5-2.5-1.5-1.4 0-2.5.8-2.5 2s1 1.7 2.5 2 2.5.9 2.5 2-1.1 2-2.5 2c-1 0-2-.5-2.5-1.5M12 6.5v11"/></svg>Subscription</a>
    <a class="active"><svg viewBox="0 0 24 24" fill="none" stroke="#fff" stroke-width="1.6"><path d="M12 2l2.5 2 3.2-.3.6 3.1 2.7 1.8-1.3 2.9 1.3 2.9-2.7 1.8-.6 3.1-3.2-.3L12 22l-2.5-2-3.2.3-.6-3.1-2.7-1.8 1.3-2.9-1.3-2.9 2.7-1.8.6-3.1 3.2.3z"/><path d="M8 12l3 3 5-6"/></svg>Verify</a>
  </nav>
  <main class="content">
    <h2 class="page-title">Verify Info</h2>
    <div class="form-box" style="width:628px;height:455px;top:139px">
      <p class="form-lead" style="top:50px">This info below will be shown on your profile page</p>
      <div class="info-row" style="top:108px"><b>Company Legal Name:</b><span>Company name here</span></div>
      <div class="info-row" style="top:142px"><b>ACN:</b><span>111111</span></div>
      <div class="info-row" style="top:175px"><b>ABN:</b><span>222222</span></div>
      <span class="label" style="left:50px;top:226px">BSB</span>
      <span class="label" style="left:338px;top:226px">ACCOUNT</span>
      <div class="round-field" style="left:47px;top:252px;width:269px">09999</div>
      <div class="round-field" style="left:333px;top:252px;width:270px">222222</div>
      <div class="check-line"><span class="box"><svg width="11" height="11" viewBox="0 0 10 10"><path d="M1.5 5l2.5 2.5 4.5-5" stroke="#666" stroke-width="1.4" fill="none"/></svg></span>Hidden</div>
      <span class="pill-btn" style="left:47px;top:371px;width:174px;height:47px">Save Verify Data</span>
    </div>
    <footer class="footer">Vaultra @ 2023</footer>
  </main>
</section>

</body>
</html>
```